Upscale business cards needed for family office

We would like professional business cards created for employees of our family office. Relatively simple and straightforward, but also with a unique element to set them apart. Probably stick with neutral and simple colors that mesh well with the colors in the logo. We need space for the traditional elements, including name, title, address, email/phone number.

Industry/Entity Type

Business

Contact Information for Business Card

Space for name, title, phone number, email, address

```html
<!DOCTYPE html>
<html lang="en">
<head>
<meta charset="utf-8">
<title>H&amp;W Business Card</title>
<link href="https://fonts.googleapis.com/css2?family=Open+Sans:wght@400;700&family=Questrial&display=swap" rel="stylesheet">
<style>
  :root {
    --backdrop: #c3d0dc;
    --card: #ebebf0;
    --teal: #1b8cbf;
    --blue: #2f6cb4;
    --ink: #4a4d52;
    --muted: #8a8c90;
  }
  html, body {
    margin: 0;
    padding: 0;
    width: 1200px;
    height: 1200px;
    overflow: hidden;
    background: var(--backdrop);
  }
  .canvas {
    position: relative;
    width: 1200px;
    height: 1200px;
  }
  .card {
    position: absolute;
    left: 100px;
    top: 277px;
    width: 1000px;
    height: 646px;
    background: var(--card);
    box-shadow: 0 10px 30px rgba(40, 60, 80, 0.18);
  }
  .accent {
    position: absolute;
    width: 18px;
  }
  .accent--top-left { left: 0; top: 0; height: 50px; background: var(--teal); }
  .accent--bottom-left { left: 0; top: 398px; height: 248px; background: var(--teal); }
  .accent--right { right: 0; top: 106px; height: 237px; background: var(--blue); }

  .brand {
    position: absolute;
    left: 83px;
    top: 106px;
    width: 223px;
    height: 237px;
    display: flex;
    align-items: center;
    justify-content: center;
    font-family: "Open Sans", sans-serif;
    font-weight: 400;
    font-size: 64px;
    color: var(--ink);
  }
  .identity {
    position: absolute;
    left: 382px;
    top: 168px;
  }
  .identity__name {
    margin: 0;
    font-family: "Open Sans", sans-serif;
    font-weight: 700;
    font-size: 36px;
    color: var(--teal);
    letter-spacing: 0.5px;
  }
  .identity__title {
    margin: 8px 0 0;
    font-family: "Open Sans", sans-serif;
    font-weight: 400;
    font-size: 25px;
    color: var(--blue);
    letter-spacing: 0.5px;
  }
  .contacts {
    position: absolute;
    left: 80px;
    top: 388px;
    width: 880px;
    margin: 0;
    padding: 0;
    list-style: none;
    font-family: "Questrial", sans-serif;
    font-size: 25px;
    color: var(--muted);
  }
  .contacts__item {
    display: flex;
    align-items: flex-start;
    margin-bottom: 24px;
    line-height: 36px;
  }
  .contacts__icon {
    flex: 0 0 50px;
    height: 36px;
    display: flex;
    align-items: center;
  }
  .contacts__text { letter-spacing: 0.5px; }
  .contacts__text--address { line-height: 42px; margin-top: -3px; }
</style>
</head>
<body>
<div class="canvas">
  <article class="card">
    <span class="accent accent--top-left"></span>
    <span class="accent accent--bottom-left"></span>
    <span class="accent accent--right"></span>

    <div class="brand">H&amp;W</div>

    <header class="identity">
      <h1 class="identity__name">VIVERRA QUAM</h1>
      <p class="identity__title">LOREM IPSUM</p>
    </header>

    <ul class="contacts">
      <li class="contacts__item">
        <span class="contacts__icon">
          <svg width="26" height="26" viewBox="0 0 24 24" aria-hidden="true"><path fill="#2f6cb4" d="M6.6 10.8a15.1 15.1 0 0 0 6.6 6.6l2.2-2.2c.3-.3.7-.4 1-.2 1.1.4 2.3.6 3.6.6.6 0 1 .4 1 1V20c0 .6-.4 1-1 1A17 17 0 0 1 3 4c0-.6.4-1 1-1h3.5c.6 0 1 .4 1 1 0 1.3.2 2.5.6 3.6.1.3 0 .7-.2 1z"/></svg>
        </span>
        <span class="contacts__text">+44 000 000 0000</span>
      </li>
      <li class="contacts__item">
        <span class="contacts__icon">
          <svg width="28" height="20" viewBox="0 0 28 20" aria-hidden="true"><rect width="28" height="20" fill="#2f6cb4"/><path d="M1 1l13 10L27 1" fill="none" stroke="#ebebf0" stroke-width="2"/><path d="M1 19l9-8M27 19l-9-8" stroke="#ebebf0" stroke-width="1.5"/></svg>
        </span>
        <span class="contacts__text">loremipsum@hwoffice.com</span>
      </li>
      <li class="contacts__item">
        <span class="contacts__icon">
          <svg width="20" height="28" viewBox="0 0 20 28" aria-hidden="true"><path fill="#2f6cb4" d="M10 0a9 9 0 0 0-9 9c0 7 9 19 9 19s9-12 9-19a9 9 0 0 0-9-9zm0 13a4 4 0 1 1 0-8 4 4 0 0 1 0 8z"/></svg>
        </span>
        <span class="contacts__text contacts__text--address">consectetur adipiscing elit. Phasellus quis orci imperdiet, blandit sapien et, condimentum odio</span>
      </li>
    </ul>
  </article>
</div>
</body>
</html>
```